Business card for Bio pharmaceutical company

Hello,
We are a bio pharmaceutical contract manufacturing company in Brisbane, Australia. Can you please create a new business card design. Please go to our website for colours http://www.veltromedix.com.au.
On the back can you include the cartoon mascot Tobi Warn and the tagline
"A Global Biopharmaceutical Contract Development Manufacturing Company"
Target Market(s)
Biotechnology
Industry/Entity Type
Pharmaceutical
Contact Information for Business Card
Karen Holbrooke
Business Development Manager
karen.holbrooke@veltromedix.com.au
1937 Mulgrave Street Kelby Queesnland 4076 Australia
T: +61 7 3591 6042
M +61 427 516 908
F +61 7 3648 2095
www.veltromedix.com.au

```html
<!DOCTYPE html>
<html lang="en">
<head>
<meta charset="utf-8">
<title>Veltromedix Business Card</title>
<link rel="stylesheet" href="https://fonts.googleapis.com/css2?family=Lato:wght@400;700&display=swap">
<style>
  :root {
    --bg: #e9e6e2;
    --card: #ffffff;
    --navy: #1d3f6e;
    --blue: #2a9fd6;
    --green: #9dc23b;
    --ink: #333a40;
    --mascot-a: #9fd6f1;
    --mascot-b: #3c9fd3;
  }
  * { box-sizing: border-box; margin: 0; padding: 0; }
  html, body {
    width: 1200px; height: 900px; overflow: hidden;
    background: var(--bg);
    font-family: "Lato", Arial, sans-serif;
  }
  .stage {
    position: relative; width: 1200px; height: 900px;
    display: flex; align-items: center; justify-content: center; gap: 50px;
  }
  .card {
    position: relative; width: 540px; height: 310px; overflow: hidden;
    background: var(--card);
    box-shadow: 0 6px 18px rgba(0,0,0,.18);
  }
  /* Front */
  .brand {
    position: absolute; right: 30px; top: 22px;
    display: flex; align-items: center; gap: 8px;
    font-weight: 700; font-size: 24px; color: var(--navy);
  }
  .brand-mark { width: 14px; height: 14px; background: var(--navy); }
  .rule {
    position: absolute; left: 0; right: 20px; top: 64px;
    height: 1px; background: var(--blue);
  }
  .person { position: absolute; left: 30px; top: 135px; }
  .person-name { font-weight: 700; font-size: 19px; color: var(--ink); }
  .person-title { font-size: 13px; color: var(--blue); margin-top: 2px; }
  .contacts {
    position: absolute; left: 30px; top: 196px;
    list-style: none; font-size: 14px; color: var(--ink); line-height: 19px;
  }
  .contacts li { display: flex; align-items: center; gap: 9px; white-space: nowrap; }
  .contacts svg { width: 13px; height: 13px; fill: var(--blue); flex: none; }
  /* Back */
  .mascot {
    position: absolute; left: 75px; top: 30px; width: 120px; height: 160px;
    border-radius: 50px;
    background: radial-gradient(ellipse at 45% 35%, var(--mascot-a), var(--mascot-b));
  }
  .back-brand {
    position: absolute; left: 68px; top: 200px;
    display: flex; align-items: center; gap: 6px;
    font-weight: 700; font-size: 17px; color: var(--navy);
  }
  .back-brand .brand-mark { width: 10px; height: 10px; }
  .web {
    position: absolute; left: 40px; top: 250px;
    font-size: 15px; color: var(--ink);
  }
  .web span { color: var(--green); }
  .tagline {
    position: absolute; left: 270px; top: 95px;
    border-left: 2px solid var(--blue); padding-left: 12px;
    font-size: 20px; line-height: 26px; color: var(--ink);
    white-space: nowrap;
  }
</style>
</head>
<body>
<main class="stage">
  <section class="card card-front">
    <div class="brand"><span>Veltromedix</span><span class="brand-mark"></span></div>
    <div class="rule"></div>
    <div class="person">
      <p class="person-name">Karen Holbrooke</p>
      <p class="person-title">Business Development Manager</p>
    </div>
    <ul class="contacts">
      <li><svg viewBox="0 0 16 16"><path d="M3 2h3l1 4-2 1a9 9 0 0 0 4 4l1-2 4 1v3c0 1-1 1-1 1A12 12 0 0 1 2 3s0-1 1-1z"/></svg>+61 7 3591 6042</li>
      <li><svg viewBox="0 0 16 16"><path d="M4 1h8v14H4zM5.5 3v9h5V3zM7 13h2v1H7z" fill-rule="evenodd"/></svg>+61 427 516 908</li>
      <li><svg viewBox="0 0 16 16"><path d="M4 1h7v4H4zM1 6h14v6h-2v3H3v-3H1zM5 10v3h6v-3z" fill-rule="evenodd"/></svg>+61 7 3648 2095</li>
      <li><svg viewBox="0 0 16 16"><path d="M1 3h14v10H1zM2.5 4.5 8 9l5.5-4.5z" fill-rule="evenodd"/></svg>karen.holbrooke@veltromedix.com.au</li>
      <li><svg viewBox="0 0 16 16"><path d="M8 1a5 5 0 0 1 5 5c0 4-5 9-5 9S3 10 3 6a5 5 0 0 1 5-5zm0 3a2 2 0 1 0 0 4 2 2 0 0 0 0-4z" fill-rule="evenodd"/></svg>1937 Mulgrave Street Kelby Queesnland 4076 Australia</li>
    </ul>
  </section>

  <section class="card card-back">
    <div class="mascot" role="img" aria-label="Company mascot illustration"></div>
    <div class="back-brand"><span>Veltromedix</span><span class="brand-mark"></span></div>
    <p class="web">www.<span>veltromedix</span>.com.au</p>
    <p class="tagline">A Global<br>Biopharmaceutical<br>Contract Development<br>Manufacturing Company</p>
  </section>
</main>
</body>
</html>
```